Graphic- Educational Visual

Bramble Dog Training has created an educational tool to help its students understand and prioritize some key concepts in their dog training.

We are requesting a visual of this tool be designed.

Name/title of tool (to be included in graphic): The Bramble Compass
Description: Funnel (inverted pyramid).

From top to bottom, the levels are called:

Connect
Develop
Progress
Refine

The diagram should also include a cycle around it to, to represent that one is always moving through the levels.

Business colours are included below to make sure the funnel's colours complement the website colours or at least don't clash:

#0AA1C7 Blue and #7FC31B Green
Purple as a secondary colour -75279C

For reference, business logo is attached.

```html
<!DOCTYPE html>
<html lang="en">
<head>
<meta charset="utf-8">
<title>The Bramble Compass – Funnel Diagram</title>
<link rel="stylesheet" href="https://fonts.googleapis.com/css2?family=Arimo:wght@700&family=Cabin:wght@600&family=Mulish:wght@300&display=swap">
<style>
  :root {
    --brand-blue: #10a2c9;
    --brand-purple: #74318f;
    --brand-green: #80c243;
    --accent-orange: #f49a3e;
    --ink-grey: #58595b;
    --paper: #ffffff;
  }
  html, body {
    margin: 0;
    padding: 0;
    overflow: hidden;
    background: var(--paper);
  }
  .canvas {
    position: relative;
    width: 1200px;
    height: 1170px;
    overflow: hidden;
    background: var(--paper);
  }
  .brand-name {
    position: absolute;
    left: 18px;
    top: 58px;
    margin: 0;
    font-family: "Arimo", Arial, sans-serif;
    font-weight: 700;
    font-size: 22px;
    line-height: 26px;
    color: var(--brand-blue);
  }
  .tool-title {
    position: absolute;
    left: 0;
    width: 100%;
    top: 160px;
    margin: 0;
    text-align: center;
    font-family: "Cabin", "Trebuchet MS", sans-serif;
    font-weight: 600;
    font-size: 62px;
    letter-spacing: 1px;
    color: var(--ink-grey);
  }
  .tool-subtitle {
    position: absolute;
    left: 0;
    width: 100%;
    top: 340px;
    margin: 0;
    text-align: center;
    font-family: "Mulish", Helvetica, sans-serif;
    font-weight: 300;
    font-size: 46px;
    color: var(--ink-grey);
  }
  .funnel {
    position: absolute;
    left: 0;
    top: 0;
  }
  .level-label {
    font-family: "Arimo", Arial, sans-serif;
    font-weight: 700;
    fill: var(--paper);
    text-anchor: middle;
  }
  .cycle-line {
    stroke: var(--ink-grey);
    stroke-width: 3;
    fill: none;
  }
  .cycle-head {
    fill: var(--ink-grey);
  }
</style>
</head>
<body>
<div class="canvas">
  <p class="brand-name">Bramble<br>Dog Training</p>

  <h1 class="tool-title">The Bramble Compass</h1>
  <h2 class="tool-subtitle">Funnel Diagram</h2>

  <svg class="funnel" width="1200" height="1170" viewBox="0 0 1200 1170" aria-label="Funnel with four levels: Connect, Develop, Progress, Refine, with arrows cycling downward on both sides">
    <g class="levels" stroke-linejoin="round">
      <polygon points="292,515 913,515 850,620 355,620" fill="var(--brand-blue)" stroke="var(--brand-blue)" stroke-width="6"/>
      <polygon points="362,628 845,628 777,731 428,731" fill="var(--brand-purple)"/>
      <polygon points="435,740 771,740 706,841 500,841" fill="var(--brand-green)"/>
      <polygon points="507,850 698,850 602,988" fill="var(--accent-orange)" stroke="var(--accent-orange)" stroke-width="4"/>
    </g>

    <text class="level-label" x="601" y="587" font-size="50">Connect</text>
    <text class="level-label" x="600" y="698" font-size="42">Develop</text>
    <text class="level-label" x="602" y="807" font-size="37">Progress</text>
    <text class="level-label" x="602" y="907" font-size="29">Refine</text>

    <g class="cycle cycle-left">
      <line class="cycle-line" x1="231" y1="518" x2="550" y2="986"/>
      <polygon class="cycle-head" points="288,598 283,571 265,584"/>
      <polygon class="cycle-head" points="416,786 411,759 393,772"/>
      <polygon class="cycle-head" points="558,998 553,971 535,984"/>
    </g>
    <g class="cycle cycle-right">
      <line class="cycle-line" x1="975" y1="518" x2="656" y2="986"/>
      <polygon class="cycle-head" points="918,600 941,586 923,573"/>
      <polygon class="cycle-head" points="790,788 813,774 795,761"/>
      <polygon class="cycle-head" points="648,998 671,984 653,971"/>
    </g>
  </svg>
</div>
</body>
</html>
```